Aid, Development & Consulting Firm

Brenvale Outhwaite Consulting Pty Ltd is a small firm in Australia whose principal works in the area of aid and development. His experience is broad ranging from aid project design and evaluation; to offering security advice in running aid operations in dangerous situations. He works with governments and private firms in conducting training for personnel travelling to work in dangerous or difficult regions. He has worked for many years with NGO's (aid organisations) and consults to the WCA. He works in locations all over the globe which include trouble spots like Iraq and Sudan, to sleepier locales like Samoa and Fiji. Being on Asia's doorstep much time is spent in Asia eg Indonesia, Vietnam. He is often called on to monitor and evaluate aid projects throughtout the globe.

Target Market(s)

Government Aid Divisions eg in Oz, KerenFund; WCA; NGO's and consulting firms who work in developing countries

Industry/Entity Type

Security

Requirements
Nice to have
• Try and incorporate a global feel without being obvious i.e. no starving children as the primary work done is a step beyond obvious aid relief. Something very simple but bold and stylish as card holder is not a "touchy" feely person
Should not have
• No starving kid type scenarios. Prefer no pictures

```html
<!DOCTYPE html>
<html lang="en">
<head>
<meta charset="utf-8">
<title>Brenvale Outhwaite Consulting – Business Card</title>
<link rel="stylesheet" href="https://fonts.googleapis.com/css2?family=Cinzel:wght@400&family=Open+Sans:wght@400&display=swap">
<style>
  :root {
    --page-bg: #e7e4df;
    --card-top: #3a3a3c;
    --card-bottom: #262627;
    --ink-light: #e9e9e9;
    --ink-muted: #a9a9a9;
    --accent: #d9622b;
  }
  * { box-sizing: border-box; margin: 0; padding: 0; }
  html, body {
    width: 1200px; height: 900px; overflow: hidden;
    background: var(--page-bg);
  }
  .canvas {
    width: 1200px; height: 900px;
    display: flex; flex-direction: column;
    align-items: center; justify-content: center; gap: 60px;
  }
  .card {
    position: relative;
    width: 560px; height: 320px;
    border-radius: 4px;
    background: linear-gradient(160deg, var(--card-top), var(--card-bottom));
    box-shadow: 0 10px 26px rgba(0,0,0,.28);
    color: var(--ink-light);
  }
  /* Front */
  .card--front {
    display: flex; align-items: center; justify-content: center;
  }
  .brand {
    text-align: center;
    font-family: "Cinzel", serif;
    font-weight: 400;
    color: var(--ink-light);
    letter-spacing: 1px;
  }
  .brand__name { font-size: 27px; line-height: 1.2; }
  .brand__entity { font-size: 14px; letter-spacing: 2px; margin-top: 4px; }
  /* Back */
  .holder {
    position: absolute; top: 48px; right: 40px; text-align: right;
  }
  .holder__name {
    font-family: "Cinzel", serif; font-size: 22px; letter-spacing: 1px;
    color: var(--ink-light);
  }
  .holder__title {
    font-family: "Open Sans", sans-serif; font-size: 14px;
    color: var(--accent); margin-top: 2px;
  }
  .contact {
    position: absolute; left: 36px; bottom: 34px;
    list-style: none;
    font-family: "Open Sans", sans-serif; font-size: 12.5px;
    color: var(--ink-light); line-height: 1.45;
  }
  .contact__item { display: flex; align-items: flex-start; gap: 9px; }
  .contact__icon { width: 12px; height: 12px; margin-top: 3px; flex: none; }
  .contact__icon * { fill: var(--accent); }
</style>
</head>
<body>
<main class="canvas">
  <section class="card card--front" aria-label="Card front">
    <div class="brand">
      <div class="brand__name">Brenvale Outhwaite</div>
      <div class="brand__entity">Consulting Pty Ltd</div>
    </div>
  </section>

  <section class="card card--back" aria-label="Card back">
    <div class="holder">
      <div class="holder__name">B. Brenvale Outhwaite</div>
      <div class="holder__title">Director</div>
    </div>
    <ul class="contact">
      <li class="contact__item">
        <svg class="contact__icon" viewBox="0 0 12 12" aria-hidden="true"><path d="M6 0.5a4 4 0 0 0-4 4c0 3 4 7 4 7s4-4 4-7a4 4 0 0 0-4-4zm0 5.6a1.6 1.6 0 1 1 0-3.2 1.6 1.6 0 0 1 0 3.2z"/></svg>
        <span>27 Harlow Street, Kensal Park,<br>SA, 5042 Australia</span>
      </li>
      <li class="contact__item">
        <svg class="contact__icon" viewBox="0 0 12 12" aria-hidden="true"><path d="M2.6 1l2 2.3-1.1 1.3c.7 1.5 1.8 2.6 3.3 3.3l1.3-1.1L10.4 9 9.3 10.8C5 10.5 1.5 7 1.2 2.7z"/></svg>
        <span>+61 8 8140 5521</span>
      </li>
      <li class="contact__item">
        <svg class="contact__icon" viewBox="0 0 12 12" aria-hidden="true"><path d="M3.5 0.5h5a1 1 0 0 1 1 1v9a1 1 0 0 1-1 1h-5a1 1 0 0 1-1-1v-9a1 1 0 0 1 1-1zm0.5 1.5v7h4v-7z"/></svg>
        <span>+61 (0) 4127 36904</span>
      </li>
      <li class="contact__item">
        <svg class="contact__icon" viewBox="0 0 12 12" aria-hidden="true"><path d="M1 2.5h10v7H1zm1 1v.4l4 2.6 4-2.6v-.4z"/></svg>
        <span>brenvaleo@mailbox.com</span>
      </li>
      <li class="contact__item">
        <svg class="contact__icon" viewBox="0 0 12 12" aria-hidden="true"><circle cx="6" cy="6" r="5.5"/></svg>
        <span>www.brenvaleconsult.com</span>
      </li>
    </ul>
  </section>
</main>
</body>
</html>
```